WE HAND MAKE AND DECORATE BEAUTIFUL CREATIVE GINGER BREAD HOUSES FOR CHRISTMAS AND CUPCAKES FOR SPECIAL OCCASIONS

Contact Information for Business Card

MAPLE AND THISTLE DESIGNS
FLORA 0467 213 809
BRENDA 0455038216

```html
<!DOCTYPE html>
<html lang="en">
<head>
<meta charset="utf-8">
<title>Maple and Thistle Designs – Business Card</title>
<link rel="stylesheet" href="https://fonts.googleapis.com/css2?family=Arimo:wght@400&display=swap">
<style>
  :root {
    --card-blush: #f6d9d8;
    --card-white: #ffffff;
    --brand-red: #c0282d;
    --band-red: #c1272d;
    --photo-warm: #b98a63;
    --photo-frost: #eae4e0;
    --photo-base: #9c958c;
  }
  * { margin: 0; padding: 0; box-sizing: border-box; }
  html, body {
    width: 1200px;
    height: 756px;
    overflow: hidden;
    background: var(--card-white);
  }
  .business-card {
    position: relative;
    width: 1200px;
    height: 756px;
    overflow: hidden;
    background:
      radial-gradient(ellipse 620px 520px at 760px 430px, var(--card-white) 0%, rgba(255,255,255,0.85) 40%, rgba(255,255,255,0) 100%),
      linear-gradient(180deg, var(--card-blush) 0%, #fbe9e8 55%, #fdf1f0 100%);
  }
  .product-photo {
    position: absolute;
    left: 0;
    top: 120px;
    width: 520px;
    height: 636px;
    background:
      radial-gradient(ellipse 300px 230px at 240px 260px, var(--photo-warm) 0%, #c9a07c 55%, rgba(201,160,124,0) 100%),
      linear-gradient(180deg, rgba(234,228,224,0) 0%, var(--photo-frost) 70%, var(--photo-base) 100%);
  }
  .brand {
    position: absolute;
    left: 560px;
    top: 118px;
    width: 540px;
    text-align: center;
  }
  .brand-name {
    font-family: "Arimo", sans-serif;
    font-size: 28px;
    line-height: 1.2;
    font-weight: 400;
    letter-spacing: 2px;
    color: var(--brand-red);
    white-space: nowrap;
  }
  .contact-band {
    position: absolute;
    left: 712px;
    top: 490px;
    width: 488px;
    height: 114px;
    background: var(--band-red);
    display: flex;
    flex-direction: column;
    justify-content: center;
    gap: 12px;
    padding-right: 62px;
  }
  .contact-line {
    display: flex;
    justify-content: flex-end;
    align-items: center;
    gap: 14px;
    font-family: "Arimo", sans-serif;
    font-size: 23px;
    color: var(--card-white);
    white-space: nowrap;
  }
  .contact-name { margin-right: 10px; }
  .phone-icon { width: 22px; height: 22px; flex: none; }
</style>
</head>
<body>
  <main class="business-card">
    <div class="product-photo" role="img" aria-label="Photograph of a decorated gingerbread house with icing, candy canes and chocolate drops"></div>

    <header class="brand">
      <h1 class="brand-name">MAPLE AND THISTLE DESIGNS</h1>
    </header>

    <section class="contact-band">
      <p class="contact-line">
        <span class="contact-name">FLORA-</span>
        <span class="contact-number">0467 213 809</span>
        <svg class="phone-icon" viewBox="0 0 24 24" aria-hidden="true">
          <circle cx="12" cy="12" r="10.5" fill="none" stroke="#fff" stroke-width="1.6"/>
          <path d="M8.6 6.8c.4-.3.9-.2 1.1.2l1 1.9c.2.4.1.8-.2 1.1l-.7.6c.6 1.3 1.6 2.4 2.9 3l.6-.7c.3-.3.8-.4 1.1-.2l1.9 1c.4.2.5.7.2 1.1l-.8 1c-.5.6-1.4.8-2.200.4-2.6-1.2-4.6-3.3-5.7-5.9-.3-.8-.1-1.6.5-2.1z" fill="#fff"/>
        </svg>
      </p>
      <p class="contact-line">
        <span class="contact-name">BRENDA-</span>
        <span class="contact-number">0455038216</span>
        <svg class="phone-icon" viewBox="0 0 24 24" aria-hidden="true">
          <circle cx="12" cy="12" r="10.5" fill="none" stroke="#fff" stroke-width="1.6"/>
          <path d="M8.6 6.8c.4-.3.9-.2 1.1.2l1 1.9c.2.4.1.8-.2 1.1l-.7.6c.6 1.3 1.6 2.4 2.9 3l.6-.7c.3-.3.8-.4 1.1-.2l1.9 1c.4.2.5.7.2 1.1l-.8 1c-.5.6-1.4.8-2.2.4-2.6-1.2-4.6-3.3-5.7-5.9-.3-.8-.1-1.6.5-2.1z" fill="#fff"/>
        </svg>
      </p>
    </section>
  </main>
</body>
</html>
```